Business Card design for an International Import Export House

We need a Business Card design for our import export business. We trade in Minerals, Metals, Rice, Sugar, Steel etc.. The design should be minimalistic. It may or may not contain the physical address. In case you want to include the physical address - 418 Verandah Heights, Marlow Sector 9, Gurgaon, Haryana, India, 122009.

Target Market(s)

Steel Mills or Steel Plants, Factories, Mining businesses, Industrial houses, Government Agencies

Industry/Entity Type

Importer

Contact Information for Business Card

Business Name - Varnel Overseas

Font styles to use
Other font styles liked:
• montserrat

Requirements
Must have
• Ravi Kandola - President
• www.varneloverseas.com
• ravi@varneloverseas.com
• +91-987-654-3217
Nice to have
• worldwide suppliers of ores

```html
<!DOCTYPE html>
<html lang="en">
<head>
<meta charset="utf-8">
<title>Varnel Overseas – Business Card</title>
<link rel="stylesheet" href="https://fonts.googleapis.com/css2?family=Roboto:wght@300;400;700&display=swap">
<style>
  :root {
    --backdrop: #9a9a9a;
    --teal-light: #66bfcc;
    --teal-dark: #3b9db1;
    --teal-mark: #7fc6d3;
    --paper: #f6f6f6;
    --ink: #2b2b2b;
    --role-ink: #123a44;
    --white: #ffffff;
  }
  * { margin: 0; padding: 0; box-sizing: border-box; }
  html, body {
    width: 1200px; height: 1200px; overflow: hidden;
    background: var(--backdrop);
  }
  .sheet {
    width: 1200px; height: 1200px;
    display: grid;
    grid-template-columns: 525px 525px;
    grid-template-rows: 300px 300px;
    gap: 60px 50px;
    justify-content: center;
    align-content: center;
  }
  .card {
    width: 525px; height: 300px;
    border-radius: 4px;
    box-shadow: 0 14px 30px rgba(0,0,0,0.25);
    position: relative;
    overflow: hidden;
  }
  .card--front {
    background: linear-gradient(135deg, var(--teal-dark) 0%, var(--teal-light) 100%);
    color: var(--white);
    font-family: "Roboto", Arial, sans-serif;
  }
  .holder { position: absolute; left: 42px; top: 52px; }
  .holder__name { font-weight: 300; font-size: 36px; letter-spacing: 0.5px; line-height: 1.1; }
  .holder__role { font-weight: 400; font-size: 17px; color: var(--role-ink); margin-top: 2px; }
  .contacts { position: absolute; left: 42px; bottom: 40px; list-style: none; }
  .contacts li {
    display: flex; align-items: center; gap: 12px;
    font-weight: 300; font-size: 18px; line-height: 30px;
  }
  .contacts svg { width: 18px; height: 18px; flex: none; }

  .card--back { background: var(--paper); }
  .brand {
    position: absolute; inset: 0;
    display: flex; flex-direction: column; align-items: center; justify-content: center; gap: 22px;
  }
  .brand__dot { width: 70px; height: 70px; border-radius: 50%; background: var(--teal-mark); }
  .brand__name {
    font-family: "Roboto", Arial, sans-serif; font-weight: 700;
    font-size: 34px; letter-spacing: 1px; text-transform: uppercase;
    color: var(--teal-mark);
  }

  .card--address {
    background: var(--paper);
    grid-column: 1 / span 2; justify-self: center;
  }
  .address {
    position: absolute; left: 42px; top: 44px;
    font-family: "Roboto", Arial, sans-serif; font-weight: 400;
    font-size: 18px; color: var(--ink); line-height: 1.5;
  }
</style>
</head>
<body>
<main class="sheet">
  <section class="card card--front" aria-label="Card front">
    <div class="holder">
      <p class="holder__name">Ravi Kandola</p>
      <p class="holder__role">President</p>
    </div>
    <ul class="contacts">
      <li>
        <svg viewBox="0 0 18 18" aria-hidden="true"><rect width="18" height="18" rx="2" fill="#fff"/><path d="M5 4c1 0 1.5 2 1.5 2.5S5.5 7.5 5.8 8.3c.6 1.5 2.4 3.3 3.9 3.9.8.3 1.3-.7 1.8-.7s2.5.5 2.5 1.5-1 1.5-2 1.5C7.5 14.5 3.5 10.5 3.5 6c0-1 .5-2 1.5-2z" fill="#3b9db1"/></svg>
        <span>+91-987-654-3217</span>
      </li>
      <li>
        <svg viewBox="0 0 18 18" aria-hidden="true"><rect width="18" height="18" rx="2" fill="#fff"/><circle cx="9" cy="9" r="5" fill="none" stroke="#3b9db1" stroke-width="1.4"/><path d="M4 9h10M9 4c-2 3-2 7 0 10M9 4c2 3 2 7 0 10" fill="none" stroke="#3b9db1" stroke-width="1.1"/></svg>
        <span>www.varneloverseas.com</span>
      </li>
      <li>
        <svg viewBox="0 0 18 18" aria-hidden="true"><rect width="18" height="18" rx="2" fill="#fff"/><rect x="3.5" y="5.5" width="11" height="7.5" fill="none" stroke="#3b9db1" stroke-width="1.3"/><path d="M3.5 5.5 9 10l5.5-4.5" fill="none" stroke="#3b9db1" stroke-width="1.3"/></svg>
        <span>ravi@varneloverseas.com</span>
      </li>
    </ul>
  </section>

  <section class="card card--back" aria-label="Card back">
    <div class="brand">
      <span class="brand__dot" aria-hidden="true"></span>
      <p class="brand__name">Varnel Overseas</p>
    </div>
  </section>

  <section class="card card--address" aria-label="Address card">
    <p class="address">418 Verandah Heights, Marlow Sector 9</p>
  </section>
</main>
</body>
</html>
```